Medical Internet Marketing Company Needs a Site!

We need a new, fresh website for our search engine optimization and social media marketing company. We specialize in helping medical practices, doctors, physicians, and hospitals with their online presence and web ranking. The site should lean towards being suited for these audiences.

We have several examples of website that we like as well as things that we like about them.

Here are sites that we enjoy.

www.brightwavelab.com

It's a good design for the site all around. The videos, buttons, and images are all excellent. They did a fine job.

- We really like their "contact us" side bar and want to include one like it on the secondary pages.

www.corvantis.net

- We don't like the "thickness" of the top navigation bar.
- We like the page colors, easy navigation, and big call to action phone number in the top right corner.

http://www.teluvo.com/

Out of all the examples provided, Teluvo is our favorite and closest look and style to what we are looking for.

- We really like the openness of the design, such as space between the text and background.

- We want a price page in a style very similar to their pricing page with the services listed and check-marks, etc. although we intend to have multiple service package columns much like Corvantis's SEO pricing page.

- The way the video fits into the home page header is very organized, simple, and attention grabbing. We intend to place a slider with videos here.

- We need a page design that will allow for an image slider like Teluvo's Features page.

Here's a great example of a medical internet marketing website: http://www.dermaplex.com/

Target Market(s)

Our target market is doctors, typically male and typically 40-45 years old. I

Industry/Entity Type

Marketing

Requirements
Must have
• The homepage should have a slider in the video. Interior pages should have a video in the very top similar to how they do it on www.brightwavelab.com

The top navigation tabs needed are:
- Home
- Solutions
- Resources
- About
- Why Quelvo
- Contact

The sidebar should have a GREAT call to action in it on interior pages.

There should be one interior page that is similar to this - http://www.teluvo.com/pricing/

There needs to be a page with multiple boxes that take up a row of the web page's body. This page will house all the case studies similar to brightwave lab's: http://www.brightwavelab.com/success-stories/case-studies/ The one exception is we want the case studies to be inside of "boxes" instead of between horizontal lines like brightwave lab's.
Nice to have
• Color, professional, and clean. GREAT use of calls to actions.

```html
<!DOCTYPE html>
<html lang="en">
<head>
<meta charset="utf-8">
<title>Quelvo — SEO Dallas Internet Marketing Company</title>
<link href="https://fonts.googleapis.com/css2?family=PT+Sans:wght@400;700&family=Ubuntu:wght@400;500&display=swap" rel="stylesheet">
<style>
:root{
  --ink:#333;
  --muted:#777;
  --light:#999;
  --hero-dark:#555;
  --hero-light:#808080;
  --orange:#f7a21b;
  --orange-dark:#e68a0a;
  --peach:#f6b37a;
  --green:#8cc63f;
  --blue:#8dd0f2;
  --band:#f3f3f3;
  --rule:#e3e3e3;
  --footer:#555;
  --footer-base:#3d3d3d;
  --footer-text:#aaa;
}
*{box-sizing:border-box;margin:0;padding:0}
html,body{width:973px;height:1200px;overflow:hidden;background:#fff}
body{font-family:"PT Sans",sans-serif;color:var(--ink)}
.page{width:1200px;height:1480px;transform:scale(0.81083);transform-origin:0 0;position:relative}
.abs{position:absolute}
h1,h2,h3{font-family:"Ubuntu",sans-serif;font-weight:400}

/* header */
.site-header{height:98px;position:relative}
.brand{left:126px;top:49px;display:flex;align-items:center;gap:8px}
.brand-mark{width:34px;height:22px;background:var(--orange)}
.brand-name{font-family:"Ubuntu",sans-serif;font-size:27px;letter-spacing:3px;color:#8a8a8a}
.main-nav{left:353px;top:58px;display:flex;gap:30px;font-size:14px;color:#666}
.main-nav .active{color:#222}
.call{right:120px;top:54px;font-size:14px;color:#888}
.call strong{font-size:17px;color:#666;margin-left:4px}

/* hero */
.hero{top:98px;left:0;width:1200px;height:270px;background:radial-gradient(ellipse at 40% 40%,var(--hero-light),var(--hero-dark) 75%)}
.hero h1{position:absolute;left:124px;top:46px;font-size:27px;color:#fff;font-weight:500}
.hero p{position:absolute;left:124px;top:86px;width:485px;font-size:17px;line-height:24px;color:#e8e8e8}
.btn{position:absolute;left:124px;top:180px;width:125px;height:36px;border-radius:3px;background:linear-gradient(var(--orange),var(--orange-dark));color:#fff;font-family:"Ubuntu",sans-serif;font-size:17px;text-align:center;line-height:36px}
.video{position:absolute;left:672px;top:21px;width:408px;height:231px;background:#fff;padding:6px}
.video-still{position:relative;width:100%;height:100%;background:linear-gradient(135deg,#6f7d4e,#a9a58a 45%,#8c8a7a 70%,#b9a27a)}
.video-title{position:absolute;left:14px;top:8px;font-family:"Ubuntu",sans-serif;font-weight:500;font-size:17px;color:#22aef0}
.video-by{position:absolute;left:14px;top:34px;font-size:11px;color:#fff}
.video-by b{color:#22aef0;font-weight:400}
.play{position:absolute;left:10px;top:170px;width:65px;height:40px;border-radius:4px;background:rgba(30,30,30,.85)}
.bar{position:absolute;left:84px;top:176px;width:300px;height:32px;border-radius:4px;background:rgba(30,30,30,.85)}
.time{position:absolute;left:80px;top:172px;background:#fff;font-size:10px;padding:0 3px;color:#222}
.player-name{position:absolute;right:16px;top:180px;color:#fff;font-family:"Ubuntu",sans-serif;font-weight:500;font-size:16px}

.stripe{top:368px;left:123px;width:960px;height:5px;display:flex}
.stripe span{flex:1}

/* services */
.services{top:373px;left:0;width:1200px;height:132px;background:linear-gradient(#fff,var(--band))}
.service{position:absolute;top:30px;width:235px}
.service h2{font-size:18px;color:#333;margin-bottom:7px;white-space:nowrap}
.service p{font-size:14px;line-height:17px;color:#444}
.svc-icon{position:absolute;top:34px;width:38px;height:32px;border-radius:3px}

/* main */
.intro{left:124px;top:535px;width:640px;font-size:14px;line-height:17px}
.intro h2{font-size:18px;margin-bottom:8px}
.intro h3{font-family:"PT Sans",sans-serif;font-weight:700;font-size:14px;margin-top:16px}
.sidebar{left:795px;top:510px;width:288px;height:362px;box-shadow:-12px 0 14px -14px rgba(0,0,0,.25)}
.sidebar h2{font-size:18px;color:#333}
.quote-photo{position:absolute;left:30px;top:62px;width:42px;height:42px;background:linear-gradient(#b8a593,#7f6e63);border-radius:2px}
.quote{position:absolute;left:83px;top:60px;width:210px;font-size:14px;line-height:17px}
.quote-by{position:absolute;left:83px;top:134px;font-size:12px}
.news{position:absolute;left:30px;top:244px;width:258px;list-style:none;font-size:14px;line-height:17px}
.news li{position:relative;padding-left:16px;margin-bottom:7px}
.news li::before{content:"";position:absolute;left:0;top:5px;border-left:4px solid #333;border-top:3px solid transparent;border-bottom:3px solid transparent}
.news li.dim{color:var(--light)}

/* testimonials */
.testimonials{top:929px;left:137px;width:916px;border-top:1px solid var(--rule)}
.testimonials h2{text-align:center;font-size:18px;margin-top:18px}
.tcard{position:absolute;top:997px;width:250px}
.tcard .mark{position:absolute;left:-37px;top:-5px;font-family:Georgia,serif;font-size:54px;line-height:40px;color:#ccc}
.tcard p{font-size:14px;line-height:18px;color:#666}
.tcard .who{margin-top:9px;color:#777}
.tcard .who b{color:#333}

/* clients */
.clients{top:1134px;left:124px;width:960px;height:118px;border-top:1px solid #ececec}
.clients .label{position:absolute;left:0;top:46px;font-size:14px}
.client{position:absolute;top:42px;display:flex;align-items:center;gap:8px;font-size:15px;color:#7a5a36;white-space:nowrap}
.client i{display:inline-block;width:20px;height:20px;border-radius:50%}
.arrow{position:absolute;top:50px;border-top:5px solid transparent;border-bottom:5px solid transparent}

/* footer */
.footer{top:1252px;left:0;width:1200px;height:176px;background:linear-gradient(var(--footer),#5e5e5e)}
.fcol{position:absolute;top:30px;font-size:14px;line-height:17px;color:var(--footer-text)}
.fcol h3{font-family:"PT Sans",sans-serif;font-weight:400;color:#fff;font-size:14px;margin-bottom:9px}
.social{display:flex;gap:12px;margin-top:4px}
.social span{width:23px;height:23px;border-radius:50%;background:#777}
.copyright{top:1428px;left:0;width:1200px;height:52px;background:var(--footer-base);color:#bbb;font-size:12px;text-align:center;line-height:56px}
</style>
</head>
<body>
<div class="page">

<header class="site-header">
  <div class="abs brand"><span class="brand-mark"></span><span class="brand-name">QUELVO</span></div>
  <nav class="abs main-nav">
    <span class="active">Home</span><span>Solutions</span><span>Resources</span><span>About</span><span>Why Quelvo</span><span>Contact</span>
  </nav>
  <div class="abs call">Call Us <strong>(555) 014-2290</strong></div>
</header>

<section class="abs hero">
  <h1>SEO Dallas Internet Marketing Company</h1>
  <p>We connect you with online customers who are looking for your products and services, and help you engage, relate to, and ultimately sell these visitors your services.</p>
  <div class="btn">Read More</div>
  <div class="video">
    <div class="video-still" role="img" aria-label="Video still of a man in a suit sitting on outdoor steps">
      <div class="video-title">SEO | Online Real Estate</div>
      <div class="video-by">from <b>Quelvo</b></div>
      <div class="play"><svg width="65" height="40"><polygon points="26,12 26,28 40,20" fill="#fff"/></svg></div>
      <div class="bar"><svg width="300" height="32"><rect x="8" y="13" width="150" height="8" fill="none" stroke="#888"/><rect x="168" y="12" width="32" height="10" fill="#22aef0"/></svg></div>
      <div class="time">01:10</div>
      <div class="player-name">playline</div>
    </div>
  </div>
</section>

<div class="abs stripe"><span style="background:var(--peach)"></span><span style="background:var(--green)"></span><span style="background:var(--blue)"></span></div>

<section class="abs services">
  <div class="svc-icon" style="left:143px;background:#dfe9f5;border:1px solid #b8c8dc" role="img" aria-label="Browser chart icon"></div>
  <div class="service" style="left:194px"><h2>Search Engine Optimization</h2><p>Search Engine Optimization is the majority of what we do.</p></div>
  <div class="svc-icon" style="left:456px;background:#9dbb7a" role="img" aria-label="Money stack icon"></div>
  <div class="service" style="left:512px"><h2>Pay Per Click Advertising</h2><p>We also integrate pay-per-click (PPC) ads and leverage them for our clients.</p></div>
  <div class="svc-icon" style="left:777px;width:32px;background:linear-gradient(90deg,#f47b20,#f7b21b 50%,#7cbf3a)" role="img" aria-label="Bar chart icon"></div>
  <div class="service" style="left:827px"><h2>Strategic Consulting</h2><p>Though fairly broad, a lot of our work is strategic consultant.</p></div>
</section>

<section class="abs intro">
  <h2>Internet Marketing In Dallas</h2>
  <p>There are several attributes that make us different from other Dallas Internet marketing companies out there:</p>
  <h3>We’re a small business just like you.</h3>
  <p>We’re big enough to have  resources readily available to ensure your project is a success, yet small enough that you don’t get lost in the shuffle of other clients.</p>
  <h3>We’re wicked smart.</h3>
  <p>It’s been our CEO’s goal from day one to build this company with people smarter and more experienced than himself (and that’s not easy to do).</p>
  <h3>We have incredible talent.</h3>
  <p>We’re full of some of the best and brightest internet marketing, computer savvy, nerdiest (that IS a word) people we could find.</p>
  <h3>We call ourselves rockstars.</h3>
  <p>You would call us computer dorks… Yeah. We’re full of it. Results that is.</p>
</section>

<aside class="abs sidebar">
  <h2 class="abs" style="left:30px;top:25px">Case Study</h2>
  <div class="quote-photo" role="img" aria-label="Client portrait"></div>
  <p class="quote">Quelvo has been a great resource for Ellison Media Group. We’ve develop an incredible relationship with them.</p>
  <p class="quote-by"><b>Mark Ellison</b> - Ellison Media Group</p>
  <div class="abs" style="left:30px;top:180px;width:258px;border-top:1px solid var(--rule)"></div>
  <h2 class="abs" style="left:30px;top:206px">Latest News</h2>
  <ul class="news">
    <li>Top 5 Social Media Fails of 2012</li>
    <li class="dim">7 Reasons You Should Have a Company Happy Hour!</li>
    <li>Medical Pratice Benefits With SEO</li>
    <li>5 Tips for Social Media Interaction</li>
  </ul>
</aside>

<section class="abs testimonials"><h2>Quelvo Testimonials</h2></section>
<div class="abs tcard" style="left:161px"><span class="mark">“</span><p>Duis autem vel eum iriure dolor in hendrerit in vulputate velit esse molestie consequat, vel illum dolore eu feugiat nulla facilisis at vero eros et accumsan.</p><p class="who"><b>Victoria</b> - St Thomas</p></div>
<div class="abs tcard" style="left:499px"><span class="mark">“</span><p>Duis autem vel eum iriure dolor in hendrerit in vulputate velit esse molestie consequat, vel illum dolore eu feugiat nulla facilisis at vero eros et accumsan.</p><p class="who"><b>Steven</b> - Ontario</p></div>
<div class="abs tcard" style="left:837px"><span class="mark">“</span><p>Duis autem vel eum iriure dolor in hendrerit in vulputate velit esse molestie consequat, vel illum dolore eu feugiat nulla facilisis at vero eros et accumsan.</p><p class="who"><b>Jackob</b> - Canada</p></div>

<section class="abs clients">
  <span class="label">Client and Case Studies</span>
  <span class="arrow" style="left:164px;border-right:5px solid #bbb"></span>
  <div class="client" style="left:198px"><i style="background:#a38a56"></i>Verana Medical</div>
  <div class="client" style="left:395px;color:#2b3f8f"><i style="background:#2b3f8f"></i>Crestline Homes</div>
  <div class="client" style="left:565px;color:#8c1d22"><i style="background:#8c1d22"></i>Ellison Media Group</div>
  <div class="client" style="left:775px;color:#111">Oakridge Dermatology</div>
  <span class="arrow" style="left:949px;border-left:5px solid #666"></span>
</section>

<footer class="abs footer">
  <div class="fcol" style="left:124px"><h3>CONTACT US</h3>Quelvo, LLC<br>208 Meridian St.Denton, Tx 76201<br>(555) 014-2290<br>hello@quelvo.com</div>
  <div class="fcol" style="left:384px"><h3>SERVICES</h3>SEO &amp; Internet Marketing Services<br>Search Engine Optimization<br>Pay Per CLick advertising<br>Strategic Consulting</div>
  <div class="fcol" style="left:645px"><h3>LINKS</h3>Company<br>Dallas SEO Company<br>Dallas Internet Marketing<br>Firm</div>
  <div class="fcol" style="left:846px"><h3>FOLLOW US</h3><div class="social"><span></span><span></span><span></span><span></span><span></span></div></div>
</footer>
<div class="abs copyright">Copyright © 2012 Quelvo, LLC. All rights reserved.</div>

</div>
</body>
</html>
```